Flyer for a marketing

We are a holistic mental health facility in need of a flyer to help promote our services and encourage more people to seek care. See the attachment to tell you more. We prefer warm green colors or rich blue. Thank you.

```html
<!DOCTYPE html>
<html lang="en">
<head>
<meta charset="utf-8">
<title>Evergreen Mind Health and Wellness Flyer</title>
<link href="https://fonts.googleapis.com/css2?family=Poppins:wght@400;500;600;700&family=Playfair+Display:wght@700;800;900&display=swap" rel="stylesheet">
<style>
:root{
  --forest:#235f33;
  --green:#3f8f4c;
  --leaf:#6fb84f;
  --mint:#a8d48a;
  --sage:#8fae98;
  --navy:#123a7c;
  --ink:#1d1d1d;
  --paper:#ffffff;
  --backdrop:#e3e3e3;
}
*{margin:0;padding:0;box-sizing:border-box}
html,body{width:1200px;height:1200px;overflow:hidden;background:var(--backdrop)}
body{position:relative;font-family:'Poppins',sans-serif;color:var(--ink)}
.flyer{position:absolute;left:188px;top:67px;width:824px;height:1068px;background:var(--paper);overflow:hidden}
.abs{position:absolute}

.brand{left:55px;top:60px;display:flex;align-items:center;gap:18px}
.brand-dot{width:70px;height:70px;border-radius:50%;background:var(--forest)}
.brand-name{font-family:'Playfair Display',serif;font-weight:700;color:var(--forest);font-size:19px;line-height:22px}

.headline-top{left:55px;top:184px;font-size:43px;letter-spacing:0.5px;line-height:48px;font-weight:400}
.headline-top b{font-weight:600}
.headline-main{left:53px;top:226px;font-family:'Playfair Display',serif;font-weight:900;font-size:76px;line-height:76px;color:var(--forest);letter-spacing:-1px}
.dots{left:55px;top:310px;display:flex;gap:4px}
.dots span{width:9px;height:9px;border-radius:50%;background:var(--leaf)}
.dots span:nth-child(4){opacity:.6}.dots span:nth-child(5){opacity:.35}
.intro-title{left:55px;top:336px;font-size:25px;font-weight:600;line-height:31px}
.intro-text{left:55px;top:402px;font-size:21px;line-height:26px}

.corner-block{left:637px;top:0;width:187px;height:212px;background:var(--forest)}
.arch-frame{left:421px;top:20px;width:357px;height:425px;background:var(--sage);border-radius:178px 178px 30px 120px}
.arch-inner{left:433px;top:32px;width:332px;height:397px;background:var(--paper);border-radius:166px 166px 22px 110px}
.arch-photo{left:443px;top:45px;width:312px;height:374px;border-radius:156px 156px 16px 100px;background:linear-gradient(160deg,#d9d4cc 0%,#4a86c5 45%,#8aa0b8 75%,#a88b6a 100%)}
.arch-lines{left:0;top:0}

.promo{left:55px;top:476px;width:328px;height:297px;border-radius:22px 0 22px 0;background:var(--navy);overflow:hidden}
.promo-photo{position:absolute;left:30px;top:90px;width:298px;height:160px;background:radial-gradient(ellipse at 55% 60%,#a57a5e 0%,#5a7fb5 45%,rgba(18,58,124,0) 75%)}
.promo-head{position:absolute;top:22px;display:flex;flex-direction:column}
.promo-head .g{color:var(--leaf);font-weight:700;font-size:21px;line-height:24px}
.promo-head .w{color:#fff;font-family:'Playfair Display',serif;font-weight:700;font-size:21px;line-height:26px}
.promo-sep{position:absolute;left:195px;top:26px;width:1px;height:42px;background:#fff;opacity:.7}
.promo-sub{position:absolute;left:27px;top:76px;color:#fff;font-size:13px;line-height:17px}
.promo-cta{position:absolute;left:0;bottom:0;width:100%;height:50px;background:rgba(35,95,51,.55);display:flex;align-items:center;padding-left:24px;gap:6px}
.cta-small{font-size:13px;line-height:13px;color:#fff}
.cta-small em{font-style:normal;color:var(--mint);font-weight:600;display:block}
.cta-tiny{font-size:6px;writing-mode:vertical-rl;color:#fff}
.cta-bar{width:1px;height:26px;background:#fff}
.cta-big{font-size:28px;font-weight:700;color:var(--mint);letter-spacing:.3px}

.why-title{left:433px;top:468px;font-family:'Playfair Display',serif;font-weight:800;font-size:24px;color:var(--ink)}
.why-title span{color:var(--navy)}
.why-item{left:433px;display:flex;align-items:center;gap:12px;width:360px}
.why-icon{flex:none;width:38px;height:38px;border-radius:50%;border:3px solid var(--navy);display:flex;align-items:center;justify-content:center}
.why-text{font-size:14.5px;line-height:16.5px;font-weight:500}

.services-title{left:0;top:788px;width:824px;display:flex;justify-content:center;align-items:center;gap:6px;font-family:'Playfair Display',serif;font-weight:800;font-size:25px}
.services-title i{display:block;width:112px;height:1px;background:var(--ink)}
.services-title span{color:var(--navy)}
.services{left:54px;top:851px;width:717px;height:78px;border-radius:22px;overflow:hidden;display:flex}
.service{display:flex;align-items:flex-end;justify-content:center;text-align:center;padding-bottom:12px;color:#fff;font-size:12.2px;font-weight:600;line-height:14.5px}
.service.dark{background:var(--forest)}
.service.light{background:var(--green)}
.svc-icon{width:41px;height:41px;border-radius:50%;background:#fff;border:3px solid var(--mint);display:flex;align-items:center;justify-content:center;top:825px}

.company{left:0;top:938px;width:824px;text-align:center;color:var(--forest);font-weight:600;font-size:14.5px}
.contact{display:flex;gap:5px;align-items:flex-start;font-size:12.5px;line-height:15px;font-weight:500}
.contact svg{flex:none;margin-top:1px}
.base-bar{left:0;bottom:0;width:824px;height:14px;background:var(--forest)}
</style>
</head>
<body>
<main class="flyer">
  <div class="corner-block abs"></div>
  <svg class="arch-lines abs" width="824" height="540" viewBox="0 0 824 540">
    <path d="M412 225 V170 Q415 55 521 25" fill="none" stroke="var(--forest)" stroke-width="1.5"/>
    <path d="M790 332 V455 H645" fill="none" stroke="var(--forest)" stroke-width="1.5"/>
  </svg>
  <div class="arch-frame abs"></div>
  <div class="arch-inner abs"></div>
  <div class="arch-photo abs" role="img" aria-label="Photo of a caring nurse comforting a distressed older patient at a table"></div>

  <div class="brand abs">
    <div class="brand-dot"></div>
    <div class="brand-name">Evergreen<br>Mind<br>Health<br>and<br>Wellness</div>
  </div>

  <div class="headline-top abs">THE <b>CARE YOU</b></div>
  <div class="headline-main abs">DESERVE</div>
  <div class="dots abs"><span></span><span></span><span></span><span></span><span></span></div>
  <div class="intro-title abs">Evergreen Mind Health<br>and Wellness</div>
  <div class="intro-text abs">where deserving patients meet<br>compassionate providers.</div>

  <section class="promo abs">
    <div class="promo-photo" role="img" aria-label="Photo of a smiling family of three embracing"></div>
    <div class="promo-head" style="left:27px"><span class="g">ACCEPTING</span><span class="w">NEW PATIENTS</span></div>
    <div class="promo-sep"></div>
    <div class="promo-head" style="left:207px"><span class="g">NO</span><span class="w">WAITING</span></div>
    <div class="promo-sub">Your mental health matters,<br>so make it a priority and</div>
    <div class="promo-cta">
      <div class="cta-small"><em>CALL US</em>TODAY</div>
      <div class="cta-tiny">FOR AN</div>
      <div class="cta-bar"></div>
      <div class="cta-big">APPOINTMENT</div>
    </div>
  </section>

  <h2 class="why-title abs">WHY <span>CHOOSE US?</span></h2>
  <div class="why-item abs" style="top:505px"><div class="why-icon"><svg width="18" height="18" viewBox="0 0 18 18"><path d="M4 9l3.5 3.5L14 5" fill="none" stroke="var(--navy)" stroke-width="1.6"/></svg></div><div class="why-text">We are an integrative holistic<br>psychiatric center.</div></div>
  <div class="why-item abs" style="top:554px"><div class="why-icon"><svg width="18" height="18" viewBox="0 0 18 18"><path d="M9 3v12M3 9h12" stroke="var(--navy)" stroke-width="1.6"/></svg></div><div class="why-text">Our mission is to provide<br>compassionate quality care.</div></div>
  <div class="why-item abs" style="top:602px"><div class="why-icon"><svg width="18" height="18" viewBox="0 0 18 18"><path d="M9 15S3 11 3 7a3 3 0 0 1 6-1 3 3 0 0 1 6 1c0 4-6 8-6 8z" fill="none" stroke="var(--navy)" stroke-width="1.4"/></svg></div><div class="why-text">We listen, care, and empower<br>you to live better.</div></div>
  <div class="why-item abs" style="top:650px"><div class="why-icon"><svg width="18" height="18" viewBox="0 0 18 18"><path d="M9 3v12M3 9h12" stroke="var(--navy)" stroke-width="1.6"/></svg></div><div class="why-text">We provide psychiatric services<br>including medication management<br>and psychotherapy.</div></div>
  <div class="why-item abs" style="top:701px"><div class="why-icon"><svg width="18" height="18" viewBox="0 0 18 18"><circle cx="9" cy="6" r="2.5" fill="none" stroke="var(--navy)" stroke-width="1.4"/><path d="M4 15c0-3 2-5 5-5s5 2 5 5" fill="none" stroke="var(--navy)" stroke-width="1.4"/></svg></div><div class="why-text">We treat both children and adults</div></div>
  <div class="why-item abs" style="top:739px"><div class="why-icon"><svg width="18" height="18" viewBox="0 0 18 18"><path d="M4 9l3.5 3.5L14 5" fill="none" stroke="var(--navy)" stroke-width="1.6"/></svg></div><div class="why-text">We accept major insurances.</div></div>

  <h2 class="services-title abs"><i></i>OUR <span>SERVICES</span><i></i></h2>
  <div class="services abs">
    <div class="service dark" style="width:157px">Comprehensive<br>Psychiatric<br>Evaluation</div>
    <div class="service light" style="width:120px">Psychiatric<br>Medication<br>Management</div>
    <div class="service dark" style="width:171px">Psychiatric Medication<br>Management Plus<br>Psychotherapy</div>
    <div class="service light" style="width:120px">Integrative<br>Psychotherapy<br>Session</div>
    <div class="service dark" style="width:149px">Ketamine<br>Assisted<br>Psychotherapy</div>
  </div>
  <div class="svc-icon abs" style="left:114px"><svg width="18" height="18" viewBox="0 0 18 18"><circle cx="8" cy="8" r="5" fill="none" stroke="#555" stroke-width="1.3"/><path d="M12 12l4 4" stroke="#555" stroke-width="1.3"/></svg></div>
  <div class="svc-icon abs" style="left:252px"><svg width="18" height="18" viewBox="0 0 18 18"><circle cx="9" cy="9" r="5" fill="none" stroke="#555" stroke-width="1.3"/><circle cx="9" cy="9" r="1.8" fill="#555"/></svg></div>
  <div class="svc-icon abs" style="left:393px"><svg width="18" height="18" viewBox="0 0 18 18"><path d="M9 3v12M3 9h12" stroke="#555" stroke-width="1.3"/></svg></div>
  <div class="svc-icon abs" style="left:543px"><svg width="18" height="18" viewBox="0 0 18 18"><circle cx="9" cy="9" r="5" fill="none" stroke="#555" stroke-width="1.3" stroke-dasharray="2 1.5"/></svg></div>
  <div class="svc-icon abs" style="left:679px"><svg width="18" height="18" viewBox="0 0 18 18"><path d="M2 13h14M4 13l3-4h6" fill="none" stroke="#555" stroke-width="1.3"/><circle cx="11" cy="5" r="2" fill="none" stroke="#555" stroke-width="1.3"/></svg></div>

  <div class="company abs">Evergreen Mind Health and Wellness, APNC</div>
  <div class="contact abs" style="left:60px;top:975px"><svg width="13" height="16" viewBox="0 0 13 16"><path d="M6.5 15S1 9 1 6a5.5 5.5 0 0 1 11 0c0 3-5.5 9-5.5 9z" fill="var(--navy)"/><circle cx="6.5" cy="6" r="2" fill="#fff"/></svg><span>1450 Maplewood Court, Suite 310<br>Fairview, CA 90210</span></div>
  <div class="contact abs" style="left:60px;top:1009px"><svg width="13" height="16" viewBox="0 0 13 16"><path d="M6.5 15S1 9 1 6a5.5 5.5 0 0 1 11 0c0 3-5.5 9-5.5 9z" fill="var(--navy)"/><circle cx="6.5" cy="6" r="2" fill="#fff"/></svg><span>812 E Orchard Ave, Brookdale, CA 90211</span></div>
  <div class="contact abs" style="left:376px;top:978px"><svg width="15" height="15" viewBox="0 0 15 15"><path d="M3 1l3 3-2 2c1 2 3 4 5 5l2-2 3 3-2 2C6 14 1 9 1 3z" fill="var(--navy)"/></svg><span>(555) 014-2286</span></div>
  <div class="contact abs" style="left:376px;top:1008px"><svg width="15" height="15" viewBox="0 0 15 15"><rect x="1" y="5" width="13" height="9" fill="var(--navy)"/><rect x="4" y="1" width="7" height="5" fill="none" stroke="var(--navy)" stroke-width="1.3"/></svg><span>(555) 017-9043</span></div>
  <div class="contact abs" style="left:521px;top:977px"><svg width="15" height="15" viewBox="0 0 15 15"><rect x="1" y="3" width="13" height="9" fill="var(--navy)"/><path d="M1 3l6.5 5L14 3" fill="none" stroke="#fff" stroke-width="1"/></svg><span>info@evergreenmindhealth.com</span></div>
  <div class="contact abs" style="left:521px;top:1007px"><svg width="15" height="15" viewBox="0 0 15 15"><circle cx="7.5" cy="7.5" r="6" fill="none" stroke="var(--navy)" stroke-width="1.3"/><path d="M1.5 7.5h12M7.5 1.5c-3 3-3 9 0 12M7.5 1.5c3 3 3 9 0 12" fill="none" stroke="var(--navy)" stroke-width="1"/></svg><span>evergreenmindhealth.com</span></div>

  <div class="base-bar abs"></div>
</main>
</body>
</html>
```